Psychology and Counselling Relationship Centre wants a Website

We need a SEO Website that is professional and simple Company Logo and colours is done and supplied

Target Market(s)

People wanting marriage Counselling / Parenting Issues / Relationship issues

Industry/Entity Type

Psychology

Coding

Coded - Design and coding required

Number of Pages Required

5+ page

Font styles to use
Other font styles liked:
• calibri

Colors
32a6d6
33b8a4
0758a5

Requirements
Must have
• Simple easy layout
• Page by page link
• Easy to navigate
• Professional and Welcoming

```html
<!DOCTYPE html>
<html lang="en">
<head>
<meta charset="utf-8">
<title>Open Heart Wellbeing – Psychology and Counselling Relationship Centre</title>
<link rel="stylesheet" href="https://fonts.googleapis.com/css2?family=Poppins:wght@600&family=Signika:wght@500;600&family=Mulish:wght@400;500&family=Roboto+Condensed:wght@400&display=swap">
<style>
:root{
  --blue:#2f74b6;
  --green:#a9cf3b;
  --teal:#33b8a4;
  --ink:#1b1b1b;
  --text:#5b5b5b;
  --line:#e6e6e6;
  --white:#ffffff;
}
*{box-sizing:border-box;margin:0;padding:0}
html,body{width:1200px;height:2844px;overflow:hidden;background:var(--white)}
body{position:relative;font-family:"Mulish",Arial,sans-serif;color:var(--text)}
.abs{position:absolute}
.decor{position:absolute;left:0;top:0;width:1200px;height:2844px}

/* header */
.brand{left:76px;top:40px;display:flex;align-items:center;gap:10px;font-family:"Signika",sans-serif;font-weight:600;font-size:20px;color:var(--blue)}
.brand-dot{width:16px;height:16px;border-radius:50%;background:var(--green)}
.nav{left:310px;top:40px;display:flex;gap:21px;font-size:15px;color:var(--ink)}
.nav a{color:inherit;text-decoration:none}
.nav a.active{color:var(--green);border-bottom:2px solid var(--green);padding-bottom:3px}

/* hero */
.hero-title{left:77px;top:256px;width:540px;font-family:"Poppins",sans-serif;font-weight:600;font-size:35px;line-height:44px;color:var(--ink)}
.hero-tags{left:79px;top:400px;font-family:"Signika",sans-serif;font-size:16px;color:var(--text)}
.hero-tags .t{color:var(--teal)}.hero-tags .g{color:var(--green)}.hero-tags .b{color:var(--blue)}

.btn{display:flex;align-items:center;justify-content:center;height:52px;border-radius:26px;background:var(--blue);font-family:"Signika",sans-serif;font-weight:600;font-size:19px;color:var(--white);letter-spacing:.3px;padding-left:10px}
.btn span{display:flex;align-items:center;justify-content:center;height:52px;width:calc(100% - 10px);border-radius:26px;background:var(--green)}
.hero-btn{left:77px;top:438px;width:297px}

.dots{left:78px;top:605px;display:flex;gap:7px}
.dots i{width:14px;height:14px;border-radius:50%;border:1px solid #bdbdbd;display:block}
.dots i.on{background:var(--teal);border-color:var(--teal)}

/* contact strip */
.contact{top:722px;width:300px}
.contact .icon{width:86px;height:72px;border-radius:36px 36px 36px 36px;display:flex;align-items:center;justify-content:center}
.contact h4{margin-top:30px;font-family:"Signika",sans-serif;font-weight:600;font-size:19px;color:var(--blue)}
.contact p{margin-top:8px;font-size:16px;color:var(--ink)}

/* sections */
.sec-title{font-family:"Signika",sans-serif;font-weight:600;font-size:38px;color:var(--blue);letter-spacing:.3px}
.sec-title em{font-style:normal;color:var(--green)}
.body-copy{font-size:13.5px;line-height:27px;color:var(--text)}

.help-title{left:528px;top:985px}
.help-copy{left:531px;top:1047px;width:450px}
.help-copy p+p{margin-top:16px}
.help-btn{left:523px;top:1352px;width:203px}

.expect-title{left:0;width:1200px;text-align:center;top:1512px}
.expect-copy{left:312px;width:576px;text-align:center;top:1569px}

.card{top:1723px;width:251px;height:270px;border-radius:8px;overflow:hidden;box-shadow:0 2px 6px rgba(0,0,0,.12)}
.card .ph{height:212px}
.card .lbl{height:58px;display:flex;align-items:center;justify-content:center;font-family:"Signika",sans-serif;font-weight:500;font-size:19px;color:var(--white)}
.services-btn{left:499px;top:2028px;width:202px}

.courses-title{left:144px;top:2163px}
.courses-copy{left:147px;top:2219px;width:445px}
.courses-btn{left:147px;top:2371px;width:202px}
.enquiry{left:148px;top:2464px;width:495px;font-family:"Roboto Condensed",sans-serif;font-size:22px;line-height:31px;color:var(--ink)}
.reach{left:150px;display:flex;align-items:center;gap:14px;font-family:"Signika",sans-serif;font-weight:600;color:var(--green)}
.reach.phone{top:2552px;font-size:25px}
.reach.mail{top:2598px;font-size:19px;font-weight:500}

.foot-line{left:77px;top:2699px;width:906px;height:1px;background:var(--line)}
.foot-brand{left:77px;top:2780px}
.copyright{left:345px;top:2764px;width:510px;text-align:center;font-size:14px;line-height:25px;color:var(--ink)}
</style>
</head>
<body>

<svg class="decor" viewBox="0 0 1200 2844">
  <defs>
    <linearGradient id="sky" x1="0" y1="0" x2="0" y2="1">
      <stop offset="0" stop-color="#6a7ba3"/><stop offset=".35" stop-color="#b99aa2"/><stop offset=".6" stop-color="#f0b073"/><stop offset=".8" stop-color="#8a7a7e"/><stop offset="1" stop-color="#3e4c66"/>
    </linearGradient>
    <radialGradient id="room" cx=".55" cy=".4" r=".8">
      <stop offset="0" stop-color="#8a5a40"/><stop offset=".45" stop-color="#a88a72"/><stop offset="1" stop-color="#c9ced8"/>
    </radialGradient>
    <radialGradient id="park" cx=".5" cy=".5" r=".8">
      <stop offset="0" stop-color="#c69a80"/><stop offset=".55" stop-color="#b7b09a"/><stop offset="1" stop-color="#7e9a5a"/>
    </radialGradient>
  </defs>

  <!-- hero bands -->
  <path fill="var(--green)" d="M900 0 H1200 V230 L760 670 Q705 720 650 660 L615 620 Q588 585 594 380 Q597 300 650 250 Z"/>
  <path fill="var(--teal)" d="M1200 222 Q1140 214 1100 255 L880 475 L960 560 L1200 322 Z"/>
  <path role="img" aria-label="Photo: person in a hoodie with arms raised towards a sunset sky" fill="url(#sky)"
        d="M852 663 C760 605 640 525 637 405 C635 335 690 298 750 298 C800 298 835 320 852 345 C870 320 905 298 955 298 C1020 298 1073 335 1071 405 C1068 525 945 605 852 663Z"/>

  <!-- who we help -->
  <path fill="var(--teal)" d="M0 1560 L350 1200 V1275 Q345 1335 300 1385 L0 1705 Z"/>
  <path role="img" aria-label="Photo: young woman talking during a counselling session" fill="url(#room)"
        d="M0 1050 Q110 952 200 956 Q378 966 378 1150 Q378 1232 312 1300 L0 1612 Z"/>

  <!-- courses -->
  <path fill="var(--blue)" d="M822 2440 Q800 2510 850 2570 L1130 2844 H1200 V2500 Z"/>
  <path role="img" aria-label="Photo: father and teenage son talking outdoors" fill="url(#park)"
        d="M1200 2160 Q1110 2100 1040 2110 Q880 2130 832 2280 Q812 2360 826 2425 L1200 2790 Z"/>
  <path fill="var(--green)" d="M960 2515 Q948 2565 990 2605 L1200 2812 V2683 L1005 2485 Q978 2478 960 2515 Z"/>
</svg>

<header>
  <div class="abs brand"><span class="brand-dot"></span>Open Heart Wellbeing</div>
  <nav class="abs nav">
    <a class="active" href="#">Home</a><a href="#">How We Can Help</a><a href="#">Relationship Counselling</a><a href="#">Parenting</a><a href="#">Courses</a><a href="#">Our Team</a><a href="#">Services</a><a href="#">Contact</a>
  </nav>
</header>

<section class="hero">
  <h1 class="abs hero-title">Open Heart<br>Psychology and Counselling<br>Relationship Centre</h1>
  <p class="abs hero-tags"><span class="t">MARRIAGE COUNSELLING</span> | <span class="g">PARENTING ISSUES</span> | <span class="b">RELATIONSHIP ISSUES</span></p>
  <a class="abs btn hero-btn"><span>BOOK AN APPOINTMENT</span></a>
  <div class="abs dots"><i></i><i class="on"></i><i></i><i></i><i></i><i></i></div>
</section>

<section class="contacts">
  <div class="abs contact" style="left:141px">
    <div class="icon" style="background:var(--blue)"><svg width="26" height="26" viewBox="0 0 24 24"><path fill="#fff" d="M6.6 10.8c1.4 2.8 3.8 5.1 6.6 6.6l2.2-2.2c.3-.3.7-.4 1-.2 1.1.4 2.3.6 3.6.6.6 0 1 .4 1 1V20c0 .6-.4 1-1 1C10.6 21 3 13.4 3 4c0-.6.4-1 1-1h3.5c.6 0 1 .4 1 1 0 1.3.2 2.5.6 3.6.1.3 0 .7-.2 1z"/></svg></div>
    <h4>Text Us :</h4><p>0400 123 456</p>
  </div>
  <div class="abs contact" style="left:454px">
    <div class="icon" style="background:var(--green)"><svg width="22" height="30" viewBox="0 0 16 24"><rect x="1" y="1" width="14" height="22" rx="2" fill="#fff"/><rect x="3" y="4" width="10" height="14" fill="var(--green)"/><circle cx="8" cy="20.5" r="1.2" fill="var(--green)"/></svg></div>
    <h4>Call Us :</h4><p>(02) 9000 1234</p>
  </div>
  <div class="abs contact" style="left:767px;width:360px">
    <div class="icon" style="background:var(--teal)"><svg width="28" height="22" viewBox="0 0 28 22"><rect width="28" height="22" rx="2" fill="#fff"/><path d="M1 2l13 10L27 2" stroke="var(--teal)" stroke-width="2.5" fill="none"/></svg></div>
    <h4>Email Us :</h4><p>hello@openheartwellbeing.com.au</p>
  </div>
</section>

<section class="who-we-help">
  <h2 class="abs sec-title help-title">WHO WE <em>HELP</em></h2>
  <div class="abs body-copy help-copy">
    <p>Open Heart Psychology and Counselling Relationship Centre is a team of highly trained professionals provide the ultimate in wellbeing treatment for children, teenagers, adults, parents and couples. We have a strong reputation for providing a warm and personalised service using research based approaches.</p>
    <p>We are passionate and dedicated to helping you get what you want out of life, and we provide life changing treatment for many people, including those experiencing issues such as anxiety, stress, relationship problems. We specialise in Perinatal Anxiety, Parenting and Child issues, Couple Relationship and Men's issues.</p>
  </div>
  <a class="abs btn help-btn"><span>LEARN MORE</span></a>
</section>

<section class="what-to-expect">
  <h2 class="abs sec-title expect-title">WHAT TO <em>EXPECT</em></h2>
  <p class="abs body-copy expect-copy">Sometimes people don't know what to expect from the counselling processes. You may wonder if your issues are too complicated, or not serious enough, or worry that the things you'll discuss will be so distressing that you'll carry the pain around with you, long after leaving the session.</p>

  <div class="abs card" style="left:77px">
    <div class="ph" role="img" aria-label="Photo: couple in a tense conversation" style="background:linear-gradient(90deg,#eceae8 0%,#d98a78 22%,#e8e2dc 48%,#c7b8a6 70%,#6f7f98 100%)"></div>
    <div class="lbl" style="background:var(--teal)">COUPLES</div>
  </div>
  <div class="abs card" style="left:342px">
    <div class="ph" role="img" aria-label="Photo: upset girl with a parent in the background" style="background:linear-gradient(90deg,#c8cfd4 0%,#b9bcc2 35%,#d8ad96 65%,#a87a66 100%)"></div>
    <div class="lbl" style="background:var(--blue)">PARENTING</div>
  </div>
  <div class="abs card" style="left:608px">
    <div class="ph" role="img" aria-label="Photo: adult client talking with a counsellor" style="background:linear-gradient(90deg,#ddd6cc 0%,#d6a8b2 35%,#c9c0ae 65%,#9c9690 100%)"></div>
    <div class="lbl" style="background:var(--blue)">ADULTS</div>
  </div>
  <div class="abs card" style="left:873px">
    <div class="ph" role="img" aria-label="Photo: thoughtful child resting on a pillow" style="background:linear-gradient(160deg,#7e8c9c 0%,#b8c2cc 35%,#e4e6ea 65%,#c8ccd2 100%)"></div>
    <div class="lbl" style="background:var(--blue)">CHILDREN &amp; TEENAGERS</div>
  </div>
  <a class="abs btn services-btn"><span>VIEW SERVICES</span></a>
</section>

<section class="courses">
  <h2 class="abs sec-title courses-title">OUR <em>COURSES</em></h2>
  <p class="abs body-copy courses-copy">Open Heart Psychology and Counselling Relationship Centre offers Courses with experienced Psychological and Human Change Facilitators to help you with any issues in being human. These 5 week courses can be a fast track and engaging way to help you gently explore yourself and /or your relationship.</p>
  <a class="abs btn courses-btn"><span>VIEW COURCES</span></a>
  <p class="abs enquiry">To make a confidential enquiry or to request an initial chat over the phone or to book an appointment:</p>
  <div class="abs reach phone"><svg width="24" height="24" viewBox="0 0 24 24"><path fill="var(--teal)" d="M6.6 10.8c1.4 2.8 3.8 5.1 6.6 6.6l2.2-2.2c.3-.3.7-.4 1-.2 1.1.4 2.3.6 3.6.6.6 0 1 .4 1 1V20c0 .6-.4 1-1 1C10.6 21 3 13.4 3 4c0-.6.4-1 1-1h3.5c.6 0 1 .4 1 1 0 1.3.2 2.5.6 3.6.1.3 0 .7-.2 1z"/></svg>(02) 9000 1234</div>
  <div class="abs reach mail"><svg width="24" height="18" viewBox="0 0 28 22"><rect width="28" height="22" rx="2" fill="var(--teal)"/><path d="M1 2l13 10L27 2" stroke="#fff" stroke-width="2.5" fill="none"/></svg>info@openheartwellbeing.com.au</div>
</section>

<footer>
  <div class="abs foot-line"></div>
  <div class="abs brand foot-brand"><span class="brand-dot"></span>Open Heart Wellbeing</div>
  <p class="abs copyright">©Open Heart Psychology and Counselling Relationship Centre -<br>2019 All Rights Reserved.</p>
</footer>

</body>
</html>
```